The Tidy Lantern Business Card

I need a business card designed for The Tidy Lantern. The company provides on site support and education to end consumers in the ins and outs of all our digital devices. We advise on product purchase, installation, maintenance and troubleshooting. Anything from cordless phones to home networks.
My initial concept is double sided with the white logo on green on one side and contact details and a small logo on the flip side (logo package attached)
Contact Details:
Miles Fenwright
Managing Director
PO Box 43
Brackton, NSW 2187
Phone: 0438 907 516
email: miles@tidylantern.com.au
web: www.tidylantern.com.au
Target Market(s)
Busy professionals and retired folks.
Industry/Entity Type
Education
Look and feel

```html
<!DOCTYPE html>
<html lang="en">
<head>
<meta charset="utf-8">
<title>The Tidy Lantern – Business Card</title>
<link href="https://fonts.googleapis.com/css2?family=Fira+Sans:ital,wght@0,400;0,500;0,600;1,500&display=swap" rel="stylesheet">
<style>
  :root {
    --leaf-green: #7ab536;
    --ink-navy: #1f2f45;
    --text-grey: #3a3f45;
    --card-white: #ffffff;
    --backdrop: #e9ebe6;
  }
  html, body {
    margin: 0;
    width: 1200px;
    height: 803px;
    overflow: hidden;
    background: var(--backdrop);
    font-family: "Fira Sans", Arial, sans-serif;
  }
  .canvas {
    position: relative;
    width: 1200px;
    height: 803px;
  }
  .card {
    position: absolute;
    top: 251px;
    width: 525px;
    height: 300px;
    background: var(--card-white);
    overflow: hidden;
    box-shadow: 0 6px 18px rgba(0,0,0,0.12);
  }
  .card--details { left: 50px; }
  .card--brand { left: 625px; }
  .card__band {
    position: absolute;
    inset: 0;
    width: 100%;
    height: 100%;
  }
  .band-fill { fill: var(--leaf-green); }

  /* contact side */
  .person {
    position: absolute;
    top: 34px;
    right: 34px;
    text-align: right;
  }
  .person__name {
    margin: 0;
    font-size: 19px;
    font-weight: 600;
    color: var(--ink-navy);
    letter-spacing: 0.2px;
  }
  .person__role {
    margin: 3px 0 0;
    font-size: 14px;
    font-weight: 500;
    font-style: italic;
    color: var(--leaf-green);
  }
  .contact-list {
    position: absolute;
    right: 30px;
    top: 118px;
    margin: 0;
    padding: 0;
    list-style: none;
  }
  .contact-list li {
    display: flex;
    justify-content: flex-end;
    align-items: center;
    gap: 10px;
    height: 22px;
    font-size: 13px;
    color: var(--text-grey);
  }
  .contact-list li.contact-list__address { margin-top: 24px; }
  .icon { width: 18px; height: 18px; flex: none; }
  .icon-fill { fill: var(--leaf-green); }
  .icon-cut { fill: none; stroke: var(--card-white); stroke-width: 1.4; }
  .wordmark--small {
    position: absolute;
    left: 30px;
    bottom: 30px;
    display: flex;
    align-items: center;
    gap: 8px;
    font-size: 22px;
    font-weight: 500;
    color: var(--ink-navy);
  }
  .wordmark__dot {
    width: 12px;
    height: 12px;
    border-radius: 50%;
    background: var(--leaf-green);
  }

  /* brand side */
  .wordmark--large {
    position: absolute;
    right: 40px;
    top: 92px;
    width: 200px;
    margin: 0;
    font-size: 38px;
    line-height: 1.05;
    font-weight: 500;
    color: var(--ink-navy);
  }
</style>
</head>
<body>
<main class="canvas">

  <section class="card card--details" aria-label="Contact side">
    <svg class="card__band" viewBox="0 0 525 300" preserveAspectRatio="none" aria-hidden="true">
      <path class="band-fill" d="M0,0 H150 C120,70 135,170 60,230 C40,246 20,256 0,262 Z"/>
    </svg>

    <div class="person">
      <h1 class="person__name">Miles Fenwright</h1>
      <p class="person__role">Managing Director</p>
    </div>

    <ul class="contact-list">
      <li>0438 907 516
        <svg class="icon" viewBox="0 0 18 18" aria-hidden="true">
          <circle class="icon-fill" cx="9" cy="9" r="9"/>
          <path class="icon-cut" d="M5,6 Q9,3 13,6 M6,8 h6 l1,5 h-8 z"/>
        </svg>
      </li>
      <li>miles@tidylantern.com.au
        <svg class="icon" viewBox="0 0 18 18" aria-hidden="true">
          <rect class="icon-fill" x="0" y="3" width="18" height="12" rx="1"/>
          <path class="icon-cut" d="M1,4 L9,10 L17,4"/>
        </svg>
      </li>
      <li>www.tidylantern.com.au
        <svg class="icon" viewBox="0 0 18 18" aria-hidden="true">
          <circle class="icon-fill" cx="9" cy="9" r="9"/>
          <path class="icon-cut" d="M2,9 H16 M9,1.5 C5,5 5,13 9,16.5 C13,13 13,5 9,1.5"/>
        </svg>
      </li>
      <li class="contact-list__address">PO Box 43, Brackton, NSW 2187
        <svg class="icon" viewBox="0 0 18 18" aria-hidden="true">
          <path class="icon-fill" d="M9,0 C4.5,0 2,3.3 2,6.8 C2,11 9,18 9,18 C9,18 16,11 16,6.8 C16,3.3 13.5,0 9,0 Z"/>
          <circle cx="9" cy="7" r="2.4" fill="#ffffff"/>
        </svg>
      </li>
    </ul>

    <div class="wordmark--small"><span class="wordmark__dot"></span>The Tidy Lantern</div>
  </section>

  <section class="card card--brand" aria-label="Logo side">
    <svg class="card__band" viewBox="0 0 525 300" preserveAspectRatio="none" aria-hidden="true">
      <path class="band-fill" d="M0,40 C150,45 250,110 285,300 H0 Z"/>
    </svg>
    <p class="wordmark--large">The Tidy Lantern</p>
  </section>

</main>
</body>
</html>
```